Clarivex glass & hardware manufacturer

Need a SEO friendly, modern & professional looking website. We are selling all kinds of glass & accessories ( Glass/ Mirror/ splash back/ pool fence/ balustrade/ hardware...we are specialised on some special glass, like curve glass,tinted glass thermal & accoustic glass...) It should has simple & crisp feeling like a glass. It must be fully functional with product display and online ordering. Please see attached confirmed logo design(Blue & white). Make sure the theme color match its feel.

Target Market(s)

Architect and designer, Builder, & Developer

Industry/Entity Type

Manufacturer

Coding

Coded - Design and coding required

Font styles to use
Serif
Sans Serif

Colors

Designer to choose colors to be used in the design.

Requirements
Must have
• Glass & hardware theme and our logo
• Here are some competitor's website for reference. (Borrow ideas but not copy : )
• 1.https://www.lumarta.com.au/about
• 2.http://www.pemberdock.com.au/
• 3.http://www.qtv.com.au/
• 4.http://www.hollowmeadfittings.com.au/
Nice to have
• Some transparent or semi transparent effects to make the website like a glass
Should not have
• No limitation for your imagination

```html
<!DOCTYPE html>
<html lang="en">
<head>
<meta charset="utf-8">
<title>Clarivex Glass &amp; Hardware</title>
<link href="https://fonts.googleapis.com/css2?family=Poppins:wght@400;500;600;700&family=Open+Sans:ital,wght@0,400;0,600;0,700;1,600&display=swap" rel="stylesheet">
<style>
:root{
  --blue:#1a5fb4;
  --blue-bright:#1e8fe0;
  --blue-deep:#114a92;
  --ink:#1f2125;
  --text:#555a60;
  --muted:#8a8f95;
  --line:#d9dce0;
  --panel:#f1f2f4;
  --white:#ffffff;
}
*{box-sizing:border-box;margin:0;padding:0}
html,body{width:1200px;height:3333px;overflow:hidden}
body{font-family:"Open Sans",sans-serif;color:var(--text);background:var(--white);position:relative}
h1,h2,h3,h4{font-family:"Poppins",sans-serif;color:var(--ink)}
.abs{position:absolute}

/* header */
.site-header{position:absolute;left:0;top:0;width:1200px;height:118px;background:var(--white);border-bottom:1px solid var(--line)}
.brand{position:absolute;left:98px;top:36px;display:flex;align-items:center;gap:12px}
.brand-mark{width:40px;height:40px;background:var(--blue)}
.brand-name{font-family:"Poppins",sans-serif;font-weight:700;font-size:32px;color:var(--blue);letter-spacing:.5px}
.tollfree{position:absolute;left:590px;top:22px;display:flex;align-items:center;gap:10px;font-size:17px;color:var(--ink);font-family:"Poppins",sans-serif}
.search{position:absolute;left:882px;top:21px;width:218px;height:30px;border:1px solid #c9ccd0;border-radius:15px;font-size:11px;color:var(--muted);padding:7px 14px}
.search svg{position:absolute;right:12px;top:8px}
.main-nav{position:absolute;top:78px;left:462px;display:flex;gap:0;font-family:"Poppins",sans-serif;font-size:14.5px;color:var(--ink);font-weight:500}
.main-nav a{color:inherit;text-decoration:none;margin-right:37px}
.main-nav a:last-child{margin-right:0}

/* hero */
.hero{position:absolute;left:0;top:118px;width:1200px;height:552px;background:linear-gradient(160deg,#7d8589 0%,#a6adb1 35%,#8c9498 60%,#5e6468 100%)}
.hero-title{position:absolute;left:0;width:1200px;top:200px;text-align:center;color:var(--white);font-family:"Poppins",sans-serif;font-weight:600;font-size:46px;line-height:54px;text-shadow:0 2px 6px rgba(0,0,0,.35)}
.btn{display:inline-block;background:var(--blue-bright);color:var(--white);font-family:"Poppins",sans-serif;font-weight:500;font-size:16px;text-decoration:none}
.hero .btn{position:absolute;left:539px;top:324px;width:122px;height:36px;line-height:36px;text-align:center;border-radius:2px}
.hero-arrow{position:absolute;left:1128px;top:280px}

/* section titles */
.section-title{position:absolute;left:0;width:1200px;text-align:center;font-weight:600;font-size:40px;letter-spacing:.5px}
.divider{position:absolute;left:480px;top:796px;width:240px;height:16px}

/* about */
.about-copy{position:absolute;left:120px;top:828px;width:960px;text-align:center;font-size:13px;line-height:25px}
.feature{position:absolute;top:960px;width:330px}
.feature-icon{position:absolute;left:0;top:0;width:84px;height:84px;border-radius:50%;background:var(--blue);display:flex;align-items:center;justify-content:center}
.feature h3{position:absolute;left:106px;top:2px;font-size:17px;font-weight:600;white-space:nowrap}
.feature p{position:absolute;left:106px;top:34px;width:210px;font-size:12.5px;line-height:25px}
.feature .more{position:absolute;left:106px;top:142px;font-size:11.5px;font-weight:700;color:var(--blue);text-decoration:none;white-space:nowrap}

/* products */
.products{position:absolute;left:0;top:1193px;width:1200px;height:950px;background:linear-gradient(180deg,#f4f5f6,#eceef0)}
.tile{position:absolute;width:318px;height:357px;border:1px solid #cdd1d5}
.tile .label{position:absolute;left:0;top:152px;width:100%;height:52px;line-height:52px;text-align:center;background:rgba(30,32,36,.55);color:var(--white);font-family:"Poppins",sans-serif;font-weight:600;font-size:20px;letter-spacing:.5px}

/* testimonials */
.testimonials{position:absolute;left:0;top:2142px;width:1200px;height:340px;background:linear-gradient(135deg,#1d66c0 0%,#1a5db0 50%,#1f68c2 100%)}
.testimonials h2{position:absolute;left:0;width:1200px;top:68px;text-align:center;color:var(--white);font-size:30px;font-weight:600}
.quote{position:absolute;left:180px;top:128px;width:840px;text-align:center;color:#e6eefa;font-size:14.5px;line-height:22px}
.quote-mark{position:absolute;left:182px;top:112px;color:var(--white);font-size:30px;font-family:Georgia,serif}
.cite{position:absolute;left:0;width:1200px;top:214px;text-align:center;color:var(--white);font-weight:600;font-style:italic;font-size:16px}
.dots{position:absolute;left:553px;top:268px;display:flex;gap:4px}
.dots span{width:30px;height:3px;background:rgba(255,255,255,.45)}
.dots span.on{background:var(--white)}

/* blog */
.post{position:absolute;top:2633px;width:310px}
.post-img{width:310px;height:186px}
.post-caption{position:absolute;left:30px;top:166px;width:250px;height:38px;background:var(--white);text-align:center;font-family:"Poppins",sans-serif;font-size:17px;color:var(--ink);line-height:44px}
.post-meta{position:absolute;left:0;top:206px;width:310px;text-align:center;font-size:12px;font-style:italic;font-weight:600;color:var(--ink)}
.post-meta .sep{margin:0 10px;font-style:normal;color:var(--muted)}
.post-excerpt{position:absolute;left:0;top:232px;width:310px;text-align:center;font-size:11.5px;line-height:20px}

/* footer */
.site-footer{position:absolute;left:0;top:2983px;width:1200px;height:282px;background:linear-gradient(180deg,#f2f3f4,#eceef0)}
.site-footer h4{font-size:17px;font-weight:600;letter-spacing:.5px;position:absolute;top:46px}
.footer-brand{position:absolute;left:98px;top:52px;display:flex;align-items:center;gap:10px}
.footer-brand .brand-mark{width:34px;height:34px}
.footer-brand .brand-name{font-size:26px}
.footer-about{position:absolute;left:98px;top:118px;width:240px;font-size:12px;line-height:19px}
.social{position:absolute;left:98px;top:198px;display:flex;gap:6px}
.social span{width:24px;height:24px;border:1.5px solid var(--ink);border-radius:50%}
.news-copy{position:absolute;left:390px;top:84px;width:240px;font-size:12px;line-height:19px}
.email-field{position:absolute;left:390px;top:138px;width:244px;height:42px;background:var(--white);border:1px solid #c9ccd0;font-size:11px;padding:13px 14px;color:var(--ink)}
.subscribe{position:absolute;left:390px;top:190px;width:122px;height:32px;line-height:32px;text-align:center;background:var(--blue);color:var(--white);font-family:"Poppins",sans-serif;font-weight:500;font-size:13px}
.contact-row{position:absolute;left:686px;display:flex;gap:12px;font-size:12.5px;line-height:19px;color:var(--ink)}
.contact-row svg{flex:none;margin-top:2px}
.quick-links{position:absolute;left:985px;top:96px;list-style:none;font-size:11.5px;color:var(--ink)}
.quick-links li{height:22px;display:flex;align-items:center;gap:12px}
.quick-links li::before{content:"";border-left:5px solid var(--ink);border-top:4px solid transparent;border-bottom:4px solid transparent}
.copyright{position:absolute;left:0;top:3265px;width:1200px;height:68px;line-height:68px;text-align:center;font-size:12px;color:var(--ink);border-top:1px solid var(--line)}
</style>
</head>
<body>

<header class="site-header">
  <div class="brand"><span class="brand-mark"></span><span class="brand-name">Clarivex</span></div>
  <div class="tollfree">
    <svg width="26" height="26" viewBox="0 0 26 26"><circle cx="13" cy="13" r="12" fill="none" stroke="#1a5fb4" stroke-width="2"/><path d="M9 7l3 3-1.5 2c1 2 2 3 4 4l2-1.5 3 3-2 2c-5 0-10.5-5.5-10.5-10.5z" fill="#1a5fb4"/></svg>
    <span>Toll-Free: (615)-208-5190</span>
  </div>
  <div class="search">Search
    <svg width="12" height="12" viewBox="0 0 12 12"><circle cx="5" cy="5" r="3.8" fill="none" stroke="#333" stroke-width="1.5"/><path d="M8 8l3 3" stroke="#333" stroke-width="1.5"/></svg>
  </div>
  <nav class="main-nav">
    <a href="#">HOME</a><a href="#">ABOUT</a><a href="#">PRODUCTS</a><a href="#">PROJECTS</a><a href="#">HARDWARE</a><a href="#">NEWS</a><a href="#">CONTACT</a>
  </nav>
</header>

<section class="hero" role="img" aria-label="Modern office interior with frameless glass partition walls">
  <h1 class="hero-title" style="color:#fff">CLARIVEX<br>GLASS &amp; HARDWARES</h1>
  <a class="btn" href="#">READ MORE</a>
  <svg class="hero-arrow" width="24" height="44" viewBox="0 0 24 44"><path d="M3 3l18 19L3 41" fill="none" stroke="#fff" stroke-width="2" opacity=".8"/></svg>
</section>

<h2 class="section-title" style="top:732px">ABOUT CLARIVEX GLASS</h2>
<svg class="divider" viewBox="0 0 240 16"><line x1="0" y1="8" x2="106" y2="8" stroke="#b8bcc1"/><line x1="134" y1="8" x2="240" y2="8" stroke="#b8bcc1"/><rect x="113" y="1" width="14" height="14" fill="#1a5fb4"/></svg>
<p class="about-copy">Sed ut perspiciatis unde omnis iste natus error sit voluptatem accusantium doloremque laudantium, totam rem aperiam, eaque ipsa quae ab illo inventore veritatis et quasi architecto beatae vitae dicta sunt explicabo. Nemo enim ipsam voluptatem quia voluptas sit aspernatur aut odit aut fugit, sed quia consequuntur magni dolores eos qui ratione voluptatem sequi nesciunt. Neque porro quisquam est, qui dolorem ipsum quia dolor sit amet, consectetur</p>

<div class="feature" style="left:98px">
  <div class="feature-icon"><svg width="40" height="40" viewBox="0 0 40 40"><path d="M28 5a8 8 0 0 0-8 10L6 29a3 3 0 0 0 5 5l14-14a8 8 0 0 0 10-8l-5 4-4-1-1-4z" fill="#fff"/></svg></div>
  <h3>EXPERT INSTALLATION</h3>
  <p>Sed ut perspiciatis unde omnis iste natus error sit voluptatem accusm doloremque laudantium, totam rem aperiam, eaque ipsa</p>
  <a class="more" href="#">READ MORE &#9656;</a>
</div>
<div class="feature" style="left:448px">
  <div class="feature-icon"><svg width="44" height="40" viewBox="0 0 44 40"><path d="M4 6l12 4v26L4 32z M40 6l-12 4v26l12-4z" fill="#fff"/><path d="M18 10h8v26h-8z" fill="none" stroke="#fff" stroke-width="2"/></svg></div>
  <h3>INSTALLATION MATERIALS</h3>
  <p>Sed ut perspiciatis unde omnis iste natus error sit voluptatem accusm doloremque laudantium, totam rem aperiam, eaque ipsa</p>
  <a class="more" href="#">READ MORE &#9656;</a>
</div>
<div class="feature" style="left:800px">
  <div class="feature-icon"><svg width="44" height="40" viewBox="0 0 44 40"><ellipse cx="20" cy="16" rx="16" ry="12" fill="#fff"/><path d="M10 25l-4 8 10-5z" fill="#fff"/><circle cx="13" cy="16" r="2" fill="#1a5fb4"/><circle cx="20" cy="16" r="2" fill="#1a5fb4"/><circle cx="27" cy="16" r="2" fill="#1a5fb4"/></svg></div>
  <h3>ADVICE</h3>
  <p>Sed ut perspiciatis unde omnis iste natus error sit voluptatem accusm doloremque laudantium, totam rem aperiam, eaque ipsa</p>
  <a class="more" href="#">READ MORE &#9656;</a>
</div>

<section class="products">
  <h2 class="section-title" style="top:50px;font-size:36px">OUR PRODUCTS</h2>
  <div class="tile" style="left:98px;top:129px;background:linear-gradient(170deg,#2f7cc6,#6fb1e0 45%,#9ab0bf 75%,#6f7d88)" role="img" aria-label="Glass building facade with entrance"><div class="label">GLASS</div></div>
  <div class="tile" style="left:442px;top:129px;background:linear-gradient(170deg,#c9c2b6,#8d8579 45%,#4e4a45 80%,#6b5a4c)" role="img" aria-label="Bedroom with mirrored sliding wardrobe"><div class="label">MIRROR</div></div>
  <div class="tile" style="left:784px;top:129px;background:linear-gradient(170deg,#e6e8ea,#b9c2c6 40%,#7a4d32 70%,#5b3a27)" role="img" aria-label="Kitchen with glass splash back"><div class="label">SPLASH BACK</div></div>
  <div class="tile" style="left:98px;top:515px;background:linear-gradient(180deg,#8b98a6,#a9b3bb 40%,#5f6a55 60%,#3e8fb5 78%,#2d2a28)" role="img" aria-label="House with swimming pool and pool fence"><div class="label">POOL FENCE</div></div>
  <div class="tile" style="left:442px;top:515px;background:linear-gradient(170deg,#efe9e2,#c9bcae 45%,#8a4e2e 75%,#6d3a22)" role="img" aria-label="Staircase with glass balustrade"><div class="label">BALUSTRADE</div></div>
  <div class="tile" style="left:784px;top:515px;background:linear-gradient(160deg,#1f4a48,#3f8f8a 45%,#2a6562 70%,#163533)" role="img" aria-label="Glass stair with steel hardware fittings"><div class="label">HARDWARE</div></div>
</section>

<section class="testimonials">
  <h2>TESTIMONIALS</h2>
  <span class="quote-mark">&ldquo;</span>
  <p class="quote">Lorem ipsum dolor sit amet, consectetur adipiscing elit, sed do eiusmod tempor incididunt ut labore et dolore magna aliqua. Ut enim ad minim veniam, quis nostrud exercitation ullamco laboris nisi ut aliquip ex ea commodo consequat. Duis aute irure dolor in reprehenderit in voluptate velit esse cillum dolore eu fugiat nulla Sed ut perspiciatis unde omnis</p>
  <p class="cite">Maren Holt - Clarivex glass &amp; hardwares</p>
  <div class="dots"><span class="on"></span><span></span><span></span></div>
</section>

<h2 class="section-title" style="top:2545px;font-size:34px">LATEST BLOG</h2>

<article class="post" style="left:98px">
  <div class="post-img" role="img" aria-label="Glass office tower facade" style="background:linear-gradient(160deg,#3a6e8e,#8fb3c4 50%,#3d6a77)"></div>
  <h3 class="post-caption">Sed ut perspiciatis unde</h3>
  <p class="post-meta">Jan 21, 2018<span class="sep">\</span>2 comments</p>
  <p class="post-excerpt">Lorem ipsum dolor sit amet, consectetur adipiscing<br>Sed blandit massa vel mauris sollicitudin</p>
</article>
<article class="post" style="left:443px">
  <div class="post-img" role="img" aria-label="Curved glass building against the sky" style="background:linear-gradient(160deg,#6f9ccc,#b7cde3 45%,#6b5546 75%,#4a3a30)"></div>
  <h3 class="post-caption">Sed ut perspiciatis unde</h3>
  <p class="post-meta">Jan 21, 2018<span class="sep">\</span>2 comments</p>
  <p class="post-excerpt">Lorem ipsum dolor sit amet, consectetur adipiscing<br>Sed blandit massa vel mauris sollicitudin</p>
</article>
<article class="post" style="left:790px">
  <div class="post-img" role="img" aria-label="Close-up of glass panel with steel standoff fittings" style="background:linear-gradient(160deg,#5a4537,#8a6e58 45%,#a9b7b0 70%,#6c7c77)"></div>
  <h3 class="post-caption">Sed ut perspiciatis unde</h3>
  <p class="post-meta">Jan 21, 2018<span class="sep">\</span>2 comments</p>
  <p class="post-excerpt">Lorem ipsum dolor sit amet, consectetur adipiscing<br>Sed blandit massa vel mauris sollicitudin</p>
</article>

<footer class="site-footer">
  <div class="footer-brand"><span class="brand-mark"></span><span class="brand-name">Clarivex</span></div>
  <p class="footer-about">Sed ut perspiciatis unde omnis iste natus error sit voluptatem accusantium dmque laudantium, totam rem aperiam.</p>
  <div class="social"><span></span><span></span><span></span><span></span></div>

  <h4 style="left:390px">SIGN UP FOR NEWSLETTER</h4>
  <p class="news-copy">Excepteur sint occaecat cupidatat non proident, sunt in culpa qui officia deserunt</p>
  <div class="email-field">Enter email</div>
  <div class="subscribe">SUBSCRIPTION</div>

  <h4 style="left:686px">CONTACT US</h4>
  <div class="contact-row" style="top:98px">
    <svg width="12" height="16" viewBox="0 0 12 16"><path d="M6 0a6 6 0 0 1 6 6c0 4-6 10-6 10S0 10 0 6a6 6 0 0 1 6-6z" fill="#1a5fb4"/><circle cx="6" cy="6" r="2" fill="#fff"/></svg>
    <span>Clarivex glass &amp; hardwares<br>418 Ferrow Lane, Dunmore, Nc.<br>27019</span>
  </div>
  <div class="contact-row" style="top:168px">
    <svg width="14" height="14" viewBox="0 0 14 14"><path d="M2 1l3 3-1.3 1.7c.8 1.8 2 3 3.6 3.6L9 8l3 3-2 2C5 13 1 9 1 3z" fill="#1a5fb4"/></svg>
    <span>Phone:&nbsp; 1-800-555-0147</span>
  </div>
  <div class="contact-row" style="top:202px">
    <svg width="14" height="12" viewBox="0 0 14 12"><rect x="0" y="1" width="14" height="10" fill="#1a5fb4"/><path d="M0 1l7 5 7-5" fill="none" stroke="#fff" stroke-width="1.2"/></svg>
    <span>hello@clarivexglass.example</span>
  </div>

  <h4 style="left:983px">QUICK LINKS</h4>
  <ul class="quick-links">
    <li>Home</li><li>Products</li><li>About us</li><li>Projects</li><li>News</li><li>Contacts</li>
  </ul>
</footer>

<div class="copyright">&copy;2018 Clarivex glass &amp; hardwares. All Rights Reserved.</div>

</body>
</html>
```